Asia based real estate financing firm needs and AWESOME design for a biz card -Harbor Lending Circle

Looking for a stylish, & corporate-looking business card for a real estate financing brokerage firm in Asia, offering global mortgage loans. I uploaded our current logos. We would like to add a splash of color (perhaps the house icon) or any other suggestions are open. For the winning designer, we have a lot of work! Thanks and best of luck!

Target Market(s)

Real estate investors globally. We want to look more like a BANK and NOT a real estate company. Please don't play up on a "house" design.

Industry/Entity Type

Banking

Contact Information for Business Card

Harbor Lending Circle
Peter Wilks
Co-Founder | Partner

14 Cassia Lane, Suite 310
Singapore 047219
www.hlc-example.asia
peterwilks@hlc-example.asia
+65 555-0142
WeChat: peterwilks

Colors

Designer to choose colors to be used in the design.

Requirements
Must have
• Must have the standard business requirements for a card; name, address, email, etc
• Can be horizontal or vertical.
Nice to have
• It would be great to see some sort of variation to the logo with a pop of color. Red is good as we're in Asia, however, other options work as well.
• Our tag line is - Lending without limits. It doesn't have to be on the card but might be nice.
• I'd like to start seeing our tagline within the cards as well. - Lending without limits.
• Also, please add our location. The location for this card is Singapore so perhaps it can be highlighted or emphasised in some way.
• Singapore | Hong Kong | Shanghai | Manila
• As we will soon open an office in Shanghai, having an option for both languages would be great.
Should not have
• I'm exceited and open to your creativity ... knock it out of the park!

```html
<!DOCTYPE html>
<html lang="en">
<head>
<meta charset="utf-8">
<title>Harbor Lending Circle – Business Card</title>
<link href="https://fonts.googleapis.com/css2?family=Cinzel:wght@400;500&family=Source+Sans+3:wght@400;600&display=swap" rel="stylesheet">
<style>
  :root {
    --backdrop: #d4d4d6;
    --card: #ffffff;
    --card-edge: #b9b9bc;
    --brand-red: #e3202a;
    --ink: #0b0b0b;
    --text-grey: #3f3f42;
    --white: #ffffff;
  }
  html, body {
    margin: 0;
    padding: 0;
    width: 1024px;
    height: 1200px;
    overflow: hidden;
    background: var(--backdrop);
  }
  .card {
    position: absolute;
    left: 68px;
    width: 888px;
    height: 507px;
    background: var(--card);
    border: 1px solid var(--card-edge);
    box-sizing: border-box;
    overflow: hidden;
  }
  .card--front { top: 68px; }
  .card--back { top: 629px; }

  /* Brand name lockup */
  .brand {
    position: absolute;
    text-align: center;
    font-family: "Cinzel", serif;
    font-weight: 500;
    color: var(--brand-red);
    line-height: 1.05;
  }
  .brand__mark {
    display: block;
    margin: 0 auto;
    background: var(--brand-red);
  }
  .brand--small {
    left: 560px;
    top: 52px;
    width: 260px;
    font-size: 31px;
  }
  .brand--small .brand__mark { width: 16px; height: 16px; margin-bottom: 18px; }
  .brand--large {
    left: 0;
    width: 888px;
    top: 168px;
    font-size: 62px;
  }
  .brand--large .brand__mark { width: 26px; height: 26px; margin-bottom: 30px; }

  /* Name band */
  .name-band {
    position: absolute;
    left: 0;
    top: 194px;
    width: 364px;
    height: 118px;
    background: var(--ink);
    border-radius: 0 59px 59px 0;
    color: var(--white);
  }
  .name-band__name {
    position: absolute;
    left: 72px;
    top: 26px;
    margin: 0;
    font-family: "Cinzel", serif;
    font-weight: 500;
    font-size: 32px;
    line-height: 1;
    letter-spacing: 0.5px;
  }
  .name-band__title {
    position: absolute;
    left: 72px;
    top: 66px;
    margin: 0;
    font-family: "Source Sans 3", sans-serif;
    font-size: 22px;
    line-height: 1;
  }
  .rule {
    position: absolute;
    left: 375px;
    top: 252px;
    width: 513px;
    height: 3px;
    background: var(--brand-red);
  }

  /* Contacts */
  .contacts {
    position: absolute;
    left: 72px;
    top: 338px;
    margin: 0;
    padding: 0;
    list-style: none;
    font-family: "Source Sans 3", sans-serif;
    font-size: 22px;
    color: var(--text-grey);
  }
  .contacts__item {
    display: flex;
    align-items: center;
    height: 35px;
  }
  .contacts__icon {
    width: 24px;
    height: 24px;
    margin-right: 14px;
    flex: none;
  }
  .contacts__item--phone { color: var(--brand-red); }
  .contacts__accent { color: var(--brand-red); font-weight: 600; }

  .address {
    position: absolute;
    right: 102px;
    top: 410px;
    margin: 0;
    text-align: right;
    font-family: "Source Sans 3", sans-serif;
    font-style: normal;
    font-size: 22px;
    line-height: 33px;
    color: var(--text-grey);
  }

  .tagline {
    position: absolute;
    left: 0;
    width: 888px;
    top: 446px;
    margin: 0;
    text-align: center;
    font-family: "Cinzel", serif;
    font-weight: 400;
    font-size: 31px;
    letter-spacing: 1px;
    color: var(--brand-red);
  }
</style>
</head>
<body>

<section class="card card--front">
  <div class="brand brand--small">
    <span class="brand__mark"></span>
    Harbor Lending<br>Circle
  </div>

  <div class="name-band">
    <h1 class="name-band__name">Peter Wilks</h1>
    <p class="name-band__title">Co-founder | Partner</p>
  </div>
  <div class="rule"></div>

  <ul class="contacts">
    <li class="contacts__item contacts__item--phone">
      <svg class="contacts__icon" viewBox="0 0 24 24" aria-hidden="true">
        <circle cx="12" cy="12" r="10.5" fill="none" stroke="#e3202a" stroke-width="1.6"/>
        <path d="M9 6.5c-1.6 1-2 3.5-.6 6.3 1.4 2.8 3.6 4.6 5.5 4.5l1.3-1.6-2.2-1.8-1.2.8c-.9-.6-1.700-1.9-2-3.1l1.1-.9-.7-2.8z" fill="#e3202a"/>
      </svg>
      +65 555-0142
    </li>
    <li class="contacts__item">
      <svg class="contacts__icon" viewBox="0 0 24 24" aria-hidden="true">
        <rect x="1.5" y="5" width="21" height="14" fill="#e3202a"/>
        <path d="M1.5 5l10.5 8 10.5-8M1.5 19l8-7M22.5 19l-8-7" fill="none" stroke="#fff" stroke-width="1.4"/>
      </svg>
      peterwilks@hlc-example.asia
    </li>
    <li class="contacts__item">
      <svg class="contacts__icon" viewBox="0 0 24 24" aria-hidden="true">
        <g fill="none" stroke="#e3202a" stroke-width="1.4">
          <circle cx="12" cy="12" r="10"/>
          <ellipse cx="12" cy="12" rx="4.5" ry="10"/>
          <path d="M2 12h20M3.5 7h17M3.5 17h17"/>
        </g>
      </svg>
      <span>www.<span class="contacts__accent">hlc-example</span>.asia</span>
    </li>
    <li class="contacts__item">
      <svg class="contacts__icon" viewBox="0 0 24 24" aria-hidden="true">
        <g fill="#fff" stroke="#e3202a" stroke-width="1.4">
          <path d="M9.5 3C5.2 3 2 5.7 2 9c0 1.8 1 3.4 2.6 4.5L4 16l2.8-1.5c.9.3 1.8.4 2.7.4"/>
          <path d="M15.5 9c3.6 0 6.5 2.3 6.5 5.2 0 1.5-.8 2.8-2.1 3.8l.5 2.2-2.4-1.3c-.8.2-1.6.4-2.5.4-3.6 0-6.5-2.3-6.5-5.1S11.9 9 15.5 9z"/>
        </g>
        <g fill="#e3202a">
          <circle cx="7" cy="7.5" r="1"/><circle cx="11.5" cy="7.5" r="1"/>
          <circle cx="13.3" cy="13.5" r=".9"/><circle cx="17.7" cy="13.5" r=".9"/>
        </g>
      </svg>
      peterwilks
    </li>
  </ul>

  <address class="address">
    14 Cassia Lane, Suite 310<br>
    Singapore 047219
  </address>
</section>

<section class="card card--back">
  <div class="brand brand--large">
    <span class="brand__mark"></span>
    Harbor Lending<br>Circle
  </div>
  <p class="tagline">Lending without limits</p>
</section>

</body>
</html>
```